Business Card Design

I need a business card, for my company that reflects fire and building.
I am a bushfire consultant, and my role is to determine a fire assessment for new houses being built, in bushfire prone areas.
Compiling a report on what building materials will need to be used, and whether or not parts of the block will need to be cleared of vegetation. I would like to see the colours of fire, and possibly a house on there as well, or maybe just fire. This will probably be used as a logo as well, and will reflect the severity of fire to housing.
Target Market(s)
New home builders residential
Industry/Entity Type
Building
Contact Information for Business Card
Emberline Advisory Coastal Range
Bushfire Consultant
Garth Pemberly
0438 261 904

```html
<!DOCTYPE html>
<html lang="en">
<head>
<meta charset="utf-8">
<title>Emberline Advisory – Business Cards</title>
<link rel="stylesheet" href="https://fonts.googleapis.com/css2?family=Montserrat:wght@400;700&display=swap">
<style>
  :root {
    --backdrop: #e9e6e1;
    --charcoal: #2b2b2b;
    --charcoal-light: #4a4a4a;
    --paper: #ffffff;
    --ink: #1f1f1f;
    --flame-orange: #f26a1b;
    --flame-peach: #f9b38a;
    --flame-red: #e3202c;
  }
  * { box-sizing: border-box; margin: 0; padding: 0; }
  html, body {
    width: 1200px;
    height: 962px;
    overflow: hidden;
    background: var(--backdrop);
    font-family: "Montserrat", sans-serif;
  }
  .canvas {
    position: relative;
    width: 1200px;
    height: 962px;
  }
  .card {
    position: absolute;
    left: 270px;
    width: 660px;
    height: 403px;
    border-radius: 4px;
    box-shadow: 0 6px 18px rgba(0, 0, 0, 0.18);
    overflow: hidden;
  }
  /* Front */
  .card--front {
    top: 50px;
    background: radial-gradient(ellipse at 55% 40%, var(--charcoal-light) 0%, var(--charcoal) 70%);
    display: flex;
    align-items: center;
    justify-content: center;
  }
  .brand {
    display: flex;
    align-items: center;
    gap: 16px;
  }
  .brand__mark {
    width: 18px;
    height: 18px;
    background: var(--flame-orange);
  }
  .brand__name {
    font-weight: 700;
    text-transform: uppercase;
    letter-spacing: 1px;
    line-height: 1;
  }
  .card--front .brand__name {
    color: var(--paper);
    font-size: 40px;
  }
  /* Back */
  .card--back {
    top: 509px;
    background: var(--paper);
  }
  .card--back .brand {
    position: absolute;
    top: 92px;
    left: 150px;
    gap: 12px;
  }
  .card--back .brand__mark {
    width: 13px;
    height: 13px;
  }
  .card--back .brand__name {
    color: var(--ink);
    font-size: 28px;
  }
  .contact {
    position: absolute;
    top: 200px;
    left: 150px;
    color: var(--ink);
    font-weight: 400;
    letter-spacing: 0.5px;
  }
  .contact__name {
    font-size: 22px;
    margin-bottom: 20px;
  }
  .contact__role,
  .contact__phone {
    font-size: 21px;
    line-height: 1.35;
  }
  .edge-band {
    position: absolute;
    left: 0;
    bottom: 0;
    width: 100%;
    height: 14px;
    background: linear-gradient(90deg, var(--flame-peach) 0%, var(--flame-orange) 35%, var(--flame-red) 100%);
  }
</style>
</head>
<body>
  <main class="canvas">
    <section class="card card--front" aria-label="Card front">
      <div class="brand">
        <span class="brand__mark"></span>
        <span class="brand__name">Emberline Advisory</span>
      </div>
    </section>

    <section class="card card--back" aria-label="Card back">
      <div class="brand">
        <span class="brand__mark"></span>
        <span class="brand__name">Emberline Advisory</span>
      </div>
      <div class="contact">
        <p class="contact__name">Garth Pemberly</p>
        <p class="contact__role">Coastal Range Bushfire Consultant</p>
        <p class="contact__phone">T 0438 261 904</p>
      </div>
      <div class="edge-band"></div>
    </section>
  </main>
</body>
</html>
```